We have a parent company, Monetary Harbor Alliance (MHA), that has other company partners. We are looking for ways to incorporate our MHA logo with our network partners, Beacon Ledger and The Blue Gate. My initial thought is to have MHA as front of card logo, and include The Blue Gate and Beacon Ledger logos on back but I'm open to ideas. Card should include website www.monetaryharborco.example (use for reference). Keywords "Tax Services" "Real Estate" "Insurance" "Investments" "Chief Financial Officer"

Industry/Entity Type

Financial

```html
<!DOCTYPE html>
<html lang="en">
<head>
<meta charset="UTF-8">
<title>Monetary Harbor Alliance – Business Card</title>
<link rel="stylesheet" href="https://fonts.googleapis.com/css2?family=Cinzel:wght@600&family=Lato:wght@400;700&display=swap">
<style>
  :root {
    --backdrop: #3b3b3b;
    --brand-red: #ec262d;
    --navy: #1f2b5c;
    --white: #ffffff;
    --partner-grey: #e4e4e4;
    --social-a: #3b5998;
    --social-b: #2a8fd0;
    --social-c: #d34836;
  }
  * { box-sizing: border-box; margin: 0; padding: 0; }
  html, body { width: 1200px; height: 750px; overflow: hidden; }
  body {
    background: var(--backdrop);
    font-family: "Lato", sans-serif;
    position: relative;
  }
  .card {
    position: absolute;
    width: 466px;
    height: 266px;
    box-shadow: 0 4px 10px rgba(0,0,0,0.45);
    overflow: hidden;
  }

  /* Front */
  .card-front { left: 367px; top: 93px; background: var(--brand-red); color: var(--white); }
  .front-mark {
    position: absolute; left: 50%; top: 70px; transform: translateX(-50%);
    width: 44px; height: 44px; border-radius: 50%; background: var(--white);
  }
  .front-name {
    position: absolute; left: 0; right: 0; top: 130px; text-align: center;
    font-family: "Cinzel", serif; font-weight: 600; font-size: 21px; letter-spacing: 0.5px;
  }
  .front-web {
    position: absolute; left: 0; right: 0; top: 214px; text-align: center;
    font-size: 11.5px; letter-spacing: 1.2px;
  }

  /* Back */
  .card-back { left: 368px; top: 406px; background: var(--white); color: var(--navy); }
  .accent-dot {
    position: absolute; left: -12px; top: 33px; width: 24px; height: 24px;
    border-radius: 50%; background: var(--brand-red);
  }
  .holder { position: absolute; left: 25px; top: 31px; }
  .holder-name { font-weight: 700; font-size: 15px; letter-spacing: 0.2px; line-height: 1.1; }
  .holder-role { color: var(--brand-red); font-size: 12px; line-height: 1.2; }
  .social { position: absolute; top: 32px; left: 363px; display: flex; gap: 10px; }
  .social span { width: 19px; height: 19px; display: block; }
  .social .s1 { background: var(--social-a); }
  .social .s2 { background: var(--social-b); }
  .social .s3 { background: var(--social-c); }
  .address { position: absolute; left: 25px; top: 128px; font-size: 12px; line-height: 15px; }
  .contacts { position: absolute; left: 25px; top: 183px; list-style: none; font-size: 12px; }
  .contacts li { display: flex; align-items: center; height: 16px; gap: 8px; }
  .contacts svg { width: 11px; height: 11px; flex: none; }
  .partner {
    position: absolute; left: 310px; width: 130px;
    display: flex; align-items: center; justify-content: center;
    font-weight: 700; color: var(--navy);
  }
  .partner-ledger { top: 92px; height: 76px; font-size: 15px; }
  .partner-gate { top: 177px; height: 49px; background: var(--partner-grey); font-size: 14px; }
  .rule { position: absolute; left: 0; right: 0; top: 238px; height: 2px; background: var(--navy); }
  .services {
    position: absolute; left: 0; right: 0; top: 243px; height: 23px;
    background: var(--brand-red); color: var(--white);
    font-size: 12px; text-align: center; line-height: 23px;
  }
</style>
</head>
<body>
  <section class="card card-front">
    <div class="front-mark"></div>
    <div class="front-name">Monetary Harbor Alliance</div>
    <div class="front-web">www.monetaryharborco.example</div>
  </section>

  <section class="card card-back">
    <div class="accent-dot"></div>
    <div class="holder">
      <div class="holder-name">DANIEL REYES</div>
      <div class="holder-role">Owner</div>
    </div>
    <div class="social"><span class="s1"></span><span class="s2"></span><span class="s3"></span></div>

    <div class="address">2480 W Alder Lane<br>Lakewood, CO 80226</div>

    <ul class="contacts">
      <li>
        <svg viewBox="0 0 12 12"><path fill="#ec262d" d="M1 4c0-2 2-3 5-3s5 1 5 3v1H8V4H4v1H1zM3 6h6l1 5H2z"/></svg>
        555-014-2736
      </li>
      <li>
        <svg viewBox="0 0 12 12"><rect x="0.5" y="2" width="11" height="8" fill="#ec262d"/><path d="M1 2.5l5 4 5-4" stroke="#fff" fill="none"/></svg>
        hello@monetaryharbor.example
      </li>
      <li>
        <svg viewBox="0 0 12 12"><circle cx="6" cy="6" r="5" fill="none" stroke="#ec262d" stroke-width="1.3"/><path d="M1 6h10M6 1c-3 3-3 7 0 10M6 1c3 3 3 7 0 10" stroke="#ec262d" fill="none" stroke-width="1"/></svg>
        www.monetaryharborco.example
      </li>
    </ul>

    <div class="partner partner-ledger">Beacon Ledger</div>
    <div class="partner partner-gate">The Blue Gate</div>

    <div class="rule"></div>
    <div class="services">Tax Services | Real Estate | Insurance | Investments | Chief Financial Officer</div>
  </section>
</body>
</html>
```